Re-design my Shearing Contract Estimate format.

The one page contract estimate is the output of a Farmer going online to our website and creating their shearing contract estimate.
The design should follow our current branding.
I have uploaded the current contract estimate design and a screen shot of our home page

```html
<!DOCTYPE html>
<html lang="en">
<head>
<meta charset="UTF-8">
<title>Shearing Contract Estimate</title>
<link href="https://fonts.googleapis.com/css2?family=Poppins:wght@400;500;600;700&display=swap" rel="stylesheet">
<style>
  :root {
    --brand-green: #21493a;
    --label-bg: #eff6f1;
    --value-bg: #cbead3;
    --page-bg: #ffffff;
    --text: #21493a;
  }
  * { margin: 0; padding: 0; box-sizing: border-box; }
  html, body {
    width: 1200px; height: 1200px; overflow: hidden;
    background: var(--page-bg);
    font-family: "Poppins", sans-serif;
    color: var(--text);
  }
  .estimate { position: relative; width: 1200px; height: 1200px; }
  .brand {
    position: absolute; top: 120px; left: 0; width: 100%;
    display: flex; justify-content: center; align-items: center; gap: 14px;
  }
  .brand-dot { width: 26px; height: 26px; border-radius: 50%; background: var(--brand-green); }
  .brand-name { font-size: 52px; font-weight: 700; color: var(--brand-green); letter-spacing: 1px; }
  .section { position: absolute; left: 206px; width: 788px; }
  .section-head {
    height: 27px; border-radius: 14px; background: var(--brand-green);
    color: #fff; font-size: 14px; font-weight: 600;
    display: flex; align-items: center; justify-content: center;
    margin-bottom: 2px;
  }
  .row {
    display: grid; grid-template-columns: 470px 313px; gap: 5px;
    height: 26px; margin-bottom: 2.8px; font-size: 14px;
  }
  .row .label {
    background: var(--label-bg); border-radius: 13px 0 0 13px;
    display: flex; align-items: center; padding-left: 20px;
  }
  .row .value {
    background: var(--value-bg); border-radius: 0 13px 13px 0;
    display: flex; align-items: center; justify-content: flex-end;
    padding-right: 23px; font-weight: 600;
  }
  .row.strong .label { font-weight: 600; }
  .contract-info { top: 297px; }
  .sheep-types { top: 392px; }
  .staff { top: 693px; }
  .price { top: 906px; }
</style>
</head>
<body>
<main class="estimate">
  <header class="brand">
    <span class="brand-dot"></span>
    <span class="brand-name">Tallora</span>
  </header>

  <section class="section contract-info">
    <div class="row strong"><div class="label">Contract No.</div><div class="value">2</div></div>
    <div class="row strong"><div class="label">Grower Details</div><div class="value"></div></div>
  </section>

  <section class="section sheep-types">
    <div class="section-head">Sheep / Shearing Type</div>
    <div class="row strong"><div class="label">Merinos</div><div class="value">20,000</div></div>
    <div class="row strong"><div class="label">XB Ewes</div><div class="value">10,000</div></div>
    <div class="row strong"><div class="label">Lambs</div><div class="value"></div></div>
    <div class="row strong"><div class="label">Full Crutch</div><div class="value"></div></div>
    <div class="row strong"><div class="label">Mkt Crutch</div><div class="value"></div></div>
    <div class="row strong"><div class="label">Rams</div><div class="value"></div></div>
    <div class="row strong"><div class="label">Total Number of Sheep</div><div class="value">30,000</div></div>
    <div class="row strong"><div class="label">Number of Shed Stands</div><div class="value">8</div></div>
  </section>

  <section class="section staff">
    <div class="section-head">Wool Staff Requirements</div>
    <div class="row"><div class="label">Wool Handler</div><div class="value">3</div></div>
    <div class="row"><div class="label">Wool Classer</div><div class="value">1</div></div>
    <div class="row"><div class="label">Wool Presser / Penner (Combined Role)</div><div class="value"></div></div>
    <div class="row"><div class="label">Wool Presser</div><div class="value">0</div></div>
    <div class="row"><div class="label">Penner</div><div class="value">1</div></div>
  </section>

  <section class="section price">
    <div class="section-head">Estimated Contract Price</div>
    <div class="row"><div class="label">Total Shearing Contract Cost</div><div class="value">$178,458.00</div></div>
    <div class="row"><div class="label">Total Wool Staff Contract Cost</div><div class="value">$38,745.00</div></div>
    <div class="row strong"><div class="label">Total Exl GST</div><div class="value">$217,203.00</div></div>
    <div class="row strong"><div class="label">Total Inc GST</div><div class="value">$238,923.00</div></div>
    <div class="row"><div class="label">Total Estimated per Sheep</div><div class="value">$7.96</div></div>
  </section>
</main>
</body>
</html>
```